Luftpolster-Versandtaschen  designen
Luftpolster-Versandtaschen designen
Zielgruppe
Es ist eine natürliche Schmerzsalbe entwickelt und hergestellt in Deutschland.
Die PELOR Salbe gibt ein zuverlässige Gefühl, durch ein innovatives Naturprodukt erstaunlich schnelle, wirkungsvolle Hilfe bei Schmerzen des Bewegungsapparates und bei Hautschäden zu erhalten und dabei gleichzeitig die Haut zu pflegen.
Aufgabenstellung
Wir möchten unsere Luftpolster-Versandtaschen gestalten lassen und das Corporate Design dort platzieren.
Ziel soll sein, das der Kunde eine hohe Aufmerksamkeit schon, vor dem Öffnen und das Vertrauen erhöht, schnelle Wiedererkennung der Marke Pelor Naturbalsam.
Die Druckdateien benötigen wir als pdf oder jedwede andere Datei mit einer Mindestauflösung von 300 dpi. Die Farbdarstellung erfolgt in CMYK. Alle Grafiken werden mittig platziert und proportional angepasst. Die genauen Maße der Versandtaschen bitte den Dokument vorlage_packbag entnehmen.
Farben / Texte / Bilder können von den Dokument (neue_webseite_alle_seiten_uebersicht) verwendet werden.
Bitte die Datei (vorlage_packbag_14d.pdf) von der Druckerei beachten.

```html
<!DOCTYPE html>
<html lang="de">
<head>
<meta charset="utf-8">
<title>Pelor Naturbalsam – Versandtasche</title>
<link href="https://fonts.googleapis.com/css2?family=Open+Sans:ital,wght@0,600;0,700;0,800;1,400;1,600&family=Arimo:wght@700&display=swap" rel="stylesheet">
<style>
  :root {
    --page: #ffffff;
    --bleed: #dadada;
    --frame: #263285;
    --ink: #111111;
    --grey-text: #8a8a8a;
    --orange-edge: #f3a553;
    --orange-mid: #f8b645;
    --orange-deep: #ec7118;
    --cream: #fff3e2;
    --badge: #efb45e;
  }
  html, body {
    margin: 0;
    padding: 0;
    width: 1200px;
    height: 1200px;
    overflow: hidden;
    background: var(--page);
  }
  .canvas {
    position: relative;
    width: 1200px;
    height: 1200px;
    font-family: "Open Sans", sans-serif;
  }
  .mailer {
    position: absolute;
    left: 351px;
    top: 254px;
    width: 497px;
    height: 691px;
    background: var(--bleed);
    border-top: 2px solid var(--frame);
    border-bottom: 1px solid #c8c8cc;
    box-sizing: border-box;
  }
  .orientation-label {
    position: absolute;
    left: 0;
    width: 100%;
    top: 27px;
    text-align: center;
    padding-left: 62px;
    box-sizing: border-box;
    font-family: "Arimo", sans-serif;
    font-weight: 700;
    font-size: 13px;
    color: #000;
  }
  .print-area {
    position: absolute;
    left: 28px;
    top: 74px;
    width: 441px;
    height: 587px;
    background: var(--page);
    border: 2px solid var(--frame);
    box-sizing: border-box;
  }
  .brand-name {
    position: absolute;
    left: 152px;
    top: 72px;
    width: 110px;
    display: flex;
    align-items: center;
    gap: 6px;
  }
  .brand-name .dot {
    flex: none;
    width: 14px;
    height: 14px;
    border-radius: 50%;
    background: var(--orange-mid);
  }
  .brand-name span {
    font-weight: 800;
    font-size: 13px;
    line-height: 1.15;
    color: var(--ink);
  }
  .hero {
    position: absolute;
    left: 100px;
    top: 157px;
    width: 237px;
    height: 230px;
    background: linear-gradient(90deg, var(--orange-edge) 0%, var(--orange-mid) 25%, var(--orange-mid) 80%, var(--orange-edge) 100%);
  }
  .hero-title {
    position: absolute;
    left: 34px;
    top: 66px;
    margin: 0;
    font-weight: 800;
    font-size: 35px;
    line-height: 29px;
    color: var(--orange-deep);
    letter-spacing: 2px;
  }
  .hero-title .spaced { letter-spacing: 12.5px; }
  .hero-claim {
    position: absolute;
    left: 34px;
    top: 127px;
    margin: 0;
    font-weight: 800;
    font-size: 20px;
    line-height: 22px;
    color: var(--cream);
    letter-spacing: 0.6px;
  }
  .tagline {
    position: absolute;
    left: 0;
    width: 100%;
    top: 399px;
    margin: 0;
    text-align: center;
    font-style: italic;
    font-weight: 600;
    font-size: 11.5px;
    line-height: 16px;
    letter-spacing: 1px;
    color: var(--grey-text);
  }
  .benefits {
    position: absolute;
    left: 96px;
    top: 441px;
    margin: 0;
    padding: 0;
    list-style: none;
  }
  .benefits li {
    display: flex;
    align-items: center;
    height: 25px;
    margin-bottom: 9px;
  }
  .benefits svg { flex: none; width: 25px; height: 25px; }
  .benefits span {
    margin-left: 5px;
    font-style: italic;
    font-weight: 600;
    font-size: 7px;
    letter-spacing: 0.5px;
    text-transform: uppercase;
    color: var(--grey-text);
  }
</style>
</head>
<body>
<div class="canvas">
  <div class="mailer">
    <div class="orientation-label">OBEN</div>
    <div class="print-area">
      <div class="brand-name"><div class="dot"></div><span>Pelor Naturbalsam</span></div>

      <div class="hero">
        <h1 class="hero-title">ALWAYS<br><span class="spaced">PELOR!</span></h1>
        <p class="hero-claim">MIT DER KRAFT<br>AUS DER NATUR</p>
      </div>

      <p class="tagline">Hält jung, macht beweglich<br>Mit der 10-Kräuter-Aktivformel</p>

      <ul class="benefits">
        <li>
          <svg viewBox="0 0 26 26" aria-hidden="true">
            <circle cx="13" cy="13" r="12.5" fill="var(--badge)"/>
            <path d="M13 5 C11 8 10.5 9.5 10.5 10.5 A2.5 2.5 0 0 0 15.5 10.5 C15.5 9.5 15 8 13 5Z" fill="none" stroke="#fff" stroke-width="0.9"/>
            <path d="M5 18 L9 15 H14 A1 1 0 0 1 14 17 H11 M14 17 L19 14.5 A1 1 0 0 1 20.5 16 L15 20 H8 L6 21" fill="none" stroke="#fff" stroke-width="0.9" stroke-linecap="round" stroke-linejoin="round"/>
          </svg>
          <span>Entspannt und regeneriert</span>
        </li>
        <li>
          <svg viewBox="0 0 26 26" aria-hidden="true">
            <circle cx="13" cy="13" r="12.5" fill="var(--badge)"/>
            <path d="M13 20 V12 M13 14 C10 14 7 12 7 9 C10 9 13 10 13 14 M13 13 C13 10 16 8 19 8 C19 11 16 13 13 13" fill="none" stroke="#fff" stroke-width="0.9" stroke-linecap="round" stroke-linejoin="round"/>
          </svg>
          <span>100% Natur</span>
        </li>
        <li>
          <svg viewBox="0 0 26 26" aria-hidden="true">
            <circle cx="13" cy="13" r="12.5" fill="var(--badge)"/>
            <path d="M6 13 H20 C20 17 17 19.5 13 19.5 C9 19.5 6 17 6 13Z M10 21 H16 M14 13 L17 5" fill="none" stroke="#fff" stroke-width="0.9" stroke-linecap="round" stroke-linejoin="round"/>
          </svg>
          <span>Stärkt, pflegt, schützt</span>
        </li>
      </ul>
    </div>
  </div>
</div>
</body>
</html>
```